Photographer Card

I'm currently doing freelance photography and i need a creative design name card especially when i attend events.
I require a design that makes a STATEMENT.
Simple, elegant and nothing like the usual name cards ive seen around (Example: with a camera/tripod etc in the design).

Photographer: Brent LW
Mobile: +65 91846257
E-mail: Brent.LW.Photography@mailvento.com
Facebook: www.friendspage.com/brent.lw.photography

Thanks for your time and hope it will turn out well! :)

Thanks for all your inputs!

Im liking the cursive feel.

Id prefer not to include the title "freelance"  :)

Also, im looking for a logo to establish myself

http://www.artnookgallery.com/art/Pebbles-Business-Card-506213847

Hi all! Thanks for the designs

"Capturing magical moments"
"Capturing magical moments that are gone forever"

Back design can be in big font "look HERE"

Maybe with focusing box 

Names can be played with horizontal and vertical.

Camera

Script

```html
<!DOCTYPE html>
<html lang="en">
<head>
<meta charset="utf-8">
<title>Brent LW — Photographer Card</title>
<link rel="stylesheet" href="https://fonts.googleapis.com/css2?family=Montserrat:wght@800&family=Oswald:wght@500&family=Roboto:wght@400&display=swap">
<style>
  :root {
    --page: #e4e3e1;
    --gold-light: #f3e3a8;
    --gold: #d9b65a;
    --gold-deep: #a7812c;
    --shadow-dark: #1c1710;
    --ink: #16120c;
    --white: #ffffff;
    --panel: rgba(255, 244, 205, 0.55);
    --rule: rgba(40, 30, 15, 0.55);
  }
  * { box-sizing: border-box; margin: 0; padding: 0; }
  html, body { width: 1200px; height: 800px; overflow: hidden; }
  body {
    background: var(--page);
    position: relative;
    font-family: "Roboto", Arial, sans-serif;
  }
  .card {
    position: absolute;
    top: 246px;
    width: 540px;
    height: 308px;
    overflow: hidden;
    box-shadow: 0 10px 26px rgba(0, 0, 0, 0.18);
  }
  .card--back { left: 40px; }
  .card--front { left: 620px; }

  .card__photo {
    position: absolute;
    inset: 0;
  }
  .card--front .card__photo {
    background:
      radial-gradient(ellipse 190px 110px at 170px 60px, rgba(28, 23, 16, 0.92), rgba(28, 23, 16, 0) 75%),
      linear-gradient(100deg, var(--gold-deep) 0%, var(--gold) 35%, var(--gold-light) 75%, #f8eec6 100%);
  }
  .card--back .card__photo {
    background:
      radial-gradient(ellipse 150px 95px at 250px 60px, rgba(28, 23, 16, 0.9), rgba(28, 23, 16, 0) 75%),
      linear-gradient(90deg, var(--shadow-dark) 0%, #4a3818 14%, var(--gold) 42%, var(--gold-light) 80%, #f8eec6 100%);
  }

  .card__band {
    position: absolute;
    left: 0; right: 0;
    top: 176px;
    height: 70px;
    background: rgba(255, 246, 212, 0.28);
  }

  .brand { position: absolute; }
  .brand__rule {
    position: absolute;
    height: 3px;
    background: var(--white);
  }
  .brand__name {
    font-family: "Montserrat", Arial, sans-serif;
    font-weight: 800;
    line-height: 1;
    white-space: nowrap;
    display: flex;
    align-items: center;
    gap: 8px;
  }
  .brand__dot {
    width: 12px; height: 12px;
    border-radius: 50%;
    background: currentColor;
  }
  .brand__title {
    font-family: "Oswald", Arial, sans-serif;
    font-weight: 500;
    color: var(--white);
    letter-spacing: 0.08em;
    text-transform: uppercase;
    white-space: nowrap;
  }

  .card--front .brand { left: 196px; top: 112px; }
  .card--front .brand__rule { left: -156px; top: 24px; width: 140px; }
  .card--front .brand__name { font-size: 46px; color: var(--ink); }
  .card--front .brand__title { font-size: 21px; margin: 10px 0 0 40px; }

  .card--back .brand { left: 66px; top: 240px; }
  .card--back .brand__rule { left: -66px; top: -14px; width: 130px; }
  .card--back .brand__name { font-size: 32px; color: var(--white); }
  .card--back .brand__title { font-size: 13px; margin: 5px 0 0 6px; }

  .contact {
    position: absolute;
    left: 206px;
    top: 74px;
    width: 320px;
    height: 140px;
    background: var(--panel);
    border-radius: 8px;
    display: flex;
  }
  .contact__icons {
    width: 44px;
    flex: none;
    border-right: 2px solid var(--rule);
    display: flex;
    flex-direction: column;
    align-items: center;
    justify-content: space-around;
    padding: 12px 0;
  }
  .contact__icons svg { width: 18px; height: 18px; }
  .contact__list {
    list-style: none;
    padding: 14px 0 14px 12px;
    display: flex;
    flex-direction: column;
    justify-content: space-between;
    font-size: 11.5px;
    color: var(--ink);
    white-space: nowrap;
  }
</style>
</head>
<body>

  <section class="card card--back" aria-label="Business card, contact side">
    <div class="card__photo" role="img" aria-label="Photograph of a vintage camera on a warm golden blurred background"></div>
    <div class="contact">
      <div class="contact__icons">
        <svg viewBox="0 0 18 18" aria-label="Social page"><rect x="2" y="2" width="14" height="14" rx="2" fill="#16120c"/></svg>
        <svg viewBox="0 0 18 18" aria-label="Phone"><rect x="5" y="1.5" width="8" height="15" rx="1.5" fill="none" stroke="#16120c" stroke-width="1.6"/><line x1="8" y1="14" x2="10" y2="14" stroke="#16120c" stroke-width="1.6"/></svg>
        <svg viewBox="0 0 18 18" aria-label="Web"><circle cx="9" cy="9" r="7" fill="none" stroke="#16120c" stroke-width="1.4"/><ellipse cx="9" cy="9" rx="3" ry="7" fill="none" stroke="#16120c" stroke-width="1.2"/><line x1="2" y1="9" x2="16" y2="9" stroke="#16120c" stroke-width="1.2"/></svg>
      </div>
      <ul class="contact__list">
        <li>www.friendspage.com/brent.lw.photography</li>
        <li>+65 91846257</li>
        <li>Brent.LW.Photography</li>
        <li>Brent.LW.Photography@mailvento.com</li>
      </ul>
    </div>
    <div class="brand">
      <span class="brand__rule"></span>
      <div class="brand__name">Brent LW</div>
      <div class="brand__title">Photographer</div>
    </div>
  </section>

  <section class="card card--front" aria-label="Business card, name side">
    <div class="card__photo" role="img" aria-label="Photograph of a vintage camera on a warm golden blurred background"></div>
    <div class="card__band"></div>
    <div class="brand">
      <span class="brand__rule"></span>
      <div class="brand__name">Brent <span class="brand__dot"></span> LW</div>
      <div class="brand__title">Photographer</div>
    </div>
  </section>

</body>
</html>
```